WordPress Design - dental products

We need a Wordpress theme for a company based in Mexico, USA and Europe. We sell orthodontic products for dental industry. We are very compromised with our customers and all our products are the better option in the market. The Quality and image are really important for us.

The idea is to have a Wordpress Website that we can manage, and our customers can get info from us. Our corporate image is based in innovation, quality and customer service.

the general idea is to have a wordpress site to manage all the info and the store is in a different system, so that we need is the wordpress site desing for the frontend. 

We will need more designs so in the future for our website, so the winner will help us for many projects.

So we hope the best design.
Updates

Hi, this "wordpress site" will be used as a homepage, the eCommerce is independent. So the design is related to corporate site. Thank you

Target Market(s)

Target: dental and orthodontic industry, academy and general customers. Private an public organizations related to medical and dental industry.
Investigators and press

Industry/Entity Type

Dental

Requirements
Must have
• Must Have Priorities:
• - Respect the logo (included)
• - Respect colors (actual website)
• - Modern style and innovated website
Nice to have
• Be funcionality, simply and easy to use, think about user interfaze (UI)
Should not have
• The design should not use old-style, serif fonts like Times New Roman. Not use cartoons, flash animations, free icons. Don't modify the logo.

```html
<!DOCTYPE html>
<html lang="en">
<head>
<meta charset="utf-8">
<title>Orto-Vela – Events</title>
<link rel="stylesheet" href="https://fonts.googleapis.com/css2?family=Roboto+Condensed:wght@700&family=Ubuntu:ital,wght@0,400;0,500;1,400&family=Noto+Sans:wght@400;700&display=swap">
<style>
  :root{
    --wine-dark:#4e0817;
    --wine:#8a1230;
    --wine-mid:#a3153a;
    --nav-top:#e0232f;
    --nav-bottom:#a70d1b;
    --panel-red:#b80b14;
    --panel-red-dark:#8c0610;
    --contact-bg:#8f1730;
    --accent-pink:#ff2e6b;
    --text-red:#7d0a12;
    --heading-red:#8b0e14;
    --white:#ffffff;
    --photo-light:#e8eef3;
    --photo-mid:#c9d6df;
  }
  *{box-sizing:border-box;margin:0;padding:0}
  html,body{width:1200px;height:1098px;overflow:hidden;background:var(--white)}
  body{position:relative;font-family:"Noto Sans",sans-serif;color:var(--text-red)}
  .abs{position:absolute}

  /* Header */
  .site-header{left:0;top:0;width:1200px;height:225px;
    background:linear-gradient(90deg,var(--wine-dark) 0%,var(--wine) 45%,var(--wine-mid) 75%,var(--wine-dark) 100%)}
  .header-curves{left:0;top:0}
  .brand-mark{left:36px;top:36px;width:77px;height:110px;border:2px solid #e9d7c4;border-radius:3px}
  .brand-name{left:118px;top:76px;font-family:"Roboto Condensed",sans-serif;font-weight:700;font-size:39px;line-height:1;color:var(--white);letter-spacing:.5px}
  .brand-tagline{left:176px;top:118px;font-family:"Ubuntu",sans-serif;font-size:14px;line-height:1;color:var(--white);letter-spacing:.6px}
  .site-title{left:422px;top:78px;font-family:"Ubuntu",sans-serif;font-style:italic;font-size:40px;line-height:1;color:var(--white)}
  .social-icon{width:27px;height:27px;border-radius:4px;box-shadow:0 1px 2px rgba(0,0,0,.4)}
  .follow-label{left:1024px;top:20px;font-family:"Ubuntu",sans-serif;font-weight:500;font-size:22px;line-height:26px;white-space:nowrap;color:var(--white);transform:rotate(38deg);transform-origin:left top}

  /* Navigation */
  .main-nav{left:0;top:171px;width:1110px;height:46px;border-radius:0 40px 6px 0;
    background:linear-gradient(180deg,var(--nav-top),var(--nav-bottom));box-shadow:0 2px 4px rgba(0,0,0,.35)}
  .nav-item{top:11px;font-family:"Ubuntu",sans-serif;font-size:18px;line-height:22px;color:var(--white);text-shadow:0 1px 1px rgba(0,0,0,.4)}
  .nav-item.active{top:9px;padding:2px 14px;border-radius:14px;color:var(--wine-dark);text-shadow:none;
    background:linear-gradient(180deg,#ffffff,#d2d2d2);box-shadow:inset 0 0 0 1px #fff}

  /* Gallery widget */
  .gallery-panel{left:26px;top:242px;width:330px;height:424px;border-radius:18px;
    background:linear-gradient(180deg,var(--panel-red) 0%,var(--panel-red-dark) 100%);border:2px solid #d8d8d8}
  .panel-title-bar{left:10px;top:8px;width:308px;height:40px;border-radius:20px;border:1px solid rgba(255,255,255,.25);
    background:linear-gradient(180deg,#e01521,#a70712)}
  .panel-title{left:22px;top:4px;font-family:"Roboto Condensed",sans-serif;font-size:25px;color:var(--white)}
  .thumb{width:86px;height:80px;border-radius:8px;border:2px solid #f1e3c8;
    background:linear-gradient(160deg,#c9a26f 0%,#a07648 50%,#8a8a2c 100%)}
  .panel-divider{left:8px;top:370px;width:310px;border-top:1px dashed #ff6b73}
  .more-link{right:26px;top:383px;font-family:"Roboto Condensed",sans-serif;font-size:17px;color:var(--white);display:flex;align-items:center;gap:6px}

  /* Contact widget */
  .contact-panel{left:25px;top:698px;width:332px;height:208px;border-radius:18px;background:var(--contact-bg)}
  .contact-title{left:26px;top:12px;font-family:"Roboto Condensed",sans-serif;font-size:25px;color:var(--accent-pink)}
  .flag{width:56px;height:38px;box-shadow:0 1px 2px rgba(0,0,0,.4)}
  .flag-us{background:repeating-linear-gradient(180deg,#c8202e 0 3px,#fff 3px 6px)}
  .flag-es{background:linear-gradient(180deg,#c60b1e 0 25%,#ffc400 25% 75%,#c60b1e 75%)}
  .contact-text{left:98px;font-family:"Noto Sans",sans-serif;font-weight:700;font-size:13px;line-height:19px;color:var(--white)}
  .contact-divider{left:10px;top:130px;width:312px;border-top:1px dashed #e04a6e}

  /* Main content */
  .content-panel{left:386px;top:240px;width:792px;height:666px;border:2px solid #e6e6e6;border-radius:18px;background:var(--white)}
  .event-heading{font-family:"Roboto Condensed",sans-serif;font-size:21px;color:var(--heading-red)}
  .event-text{font-size:12px;line-height:19.2px;letter-spacing:-.1px;color:var(--text-red)}
  .event-text p+p{margin-top:19.2px}
  .event-text strong{font-weight:700}
  .event-photo{left:938px;top:305px;width:230px;height:235px;border-radius:8px;border:5px solid #f3f3f3;
    box-shadow:0 0 3px rgba(0,0,0,.2);background:linear-gradient(135deg,var(--photo-light) 0%,#f6f1ea 45%,var(--photo-mid) 100%)}
  .event-divider{left:403px;width:760px;border-top:1px dashed var(--text-red)}

  /* Footer */
  .site-footer{left:0;top:946px;width:1200px;height:152px;
    background:linear-gradient(90deg,var(--wine-dark) 0%,var(--wine) 45%,var(--wine-mid) 75%,var(--wine-dark) 100%)}
  .footer-note{left:0;top:38px;width:1176px;text-align:center;font-size:12.5px;color:var(--white)}
</style>
</head>
<body>

<header class="abs site-header">
  <svg class="abs header-curves" width="1200" height="225" viewBox="0 0 1200 225" aria-hidden="true">
    <path d="M0 40 C300 -10 700 70 1200 10" fill="none" stroke="rgba(255,255,255,.08)" stroke-width="30"/>
    <path d="M650 225 C800 120 1000 60 1200 90" fill="none" stroke="rgba(0,0,0,.18)" stroke-width="40"/>
    <path d="M0 150 C250 120 500 150 700 130" fill="none" stroke="rgba(255,255,255,.06)" stroke-width="20"/>
  </svg>
  <div class="abs brand-mark"></div>
  <div class="abs brand-name">Orto-Vela</div>
  <div class="abs brand-tagline">TODO EN ORTODONCIA...</div>
  <div class="abs site-title">Lorem Ipsum Dolor Sit Amet</div>

  <div class="abs social-icon" style="left:936px;top:34px;background:#5fb8de"></div>
  <div class="abs social-icon" style="left:971px;top:53px;background:#1f3f8f"></div>
  <div class="abs social-icon" style="left:1006px;top:71px;background:#1b6fa8"></div>
  <div class="abs social-icon" style="left:1040px;top:94px;background:#3b5b9e"></div>
  <div class="abs social-icon" style="left:1076px;top:119px;background:#ef7d22"></div>
  <div class="abs social-icon" style="left:1109px;top:144px;background:#d9d9d9"></div>
  <div class="abs follow-label">Follow us on</div>

  <nav class="abs main-nav">
    <span class="abs nav-item" style="left:36px">Home</span>
    <span class="abs nav-item" style="left:115px">About Us</span>
    <span class="abs nav-item" style="left:222px">Press</span>
    <span class="abs nav-item active" style="left:283px">Events</span>
    <span class="abs nav-item" style="left:381px">Gallery</span>
    <span class="abs nav-item" style="left:469px">Distributors</span>
    <span class="abs nav-item" style="left:603px">News</span>
    <span class="abs nav-item" style="left:668px">Blog</span>
    <span class="abs nav-item" style="left:735px">Rss</span>
    <span class="abs nav-item" style="left:794px">Social Networks</span>
    <span class="abs nav-item" style="left:955px">Contact Us</span>
  </nav>
</header>

<aside class="abs gallery-panel">
  <div class="abs panel-title-bar"><span class="abs panel-title">Gallery</span></div>
  <div class="abs thumb" style="left:20px;top:65px" role="img" aria-label="Gallery photo"></div>
  <div class="abs thumb" style="left:122px;top:65px" role="img" aria-label="Gallery photo"></div>
  <div class="abs thumb" style="left:221px;top:65px" role="img" aria-label="Gallery photo"></div>
  <div class="abs thumb" style="left:20px;top:164px" role="img" aria-label="Gallery photo"></div>
  <div class="abs thumb" style="left:122px;top:164px" role="img" aria-label="Gallery photo"></div>
  <div class="abs thumb" style="left:221px;top:164px" role="img" aria-label="Gallery photo"></div>
  <div class="abs thumb" style="left:20px;top:262px" role="img" aria-label="Gallery photo"></div>
  <div class="abs thumb" style="left:122px;top:262px" role="img" aria-label="Gallery photo"></div>
  <div class="abs thumb" style="left:221px;top:262px" role="img" aria-label="Gallery photo"></div>
  <div class="abs panel-divider"></div>
  <div class="abs more-link">View More Photos
    <svg width="16" height="16" viewBox="0 0 16 16" aria-hidden="true"><circle cx="8" cy="8" r="8" fill="#fff"/><path d="M6 4.5 L10 8 L6 11.5" fill="none" stroke="#a70712" stroke-width="2.2"/></svg>
  </div>
</aside>

<aside class="abs contact-panel">
  <div class="abs contact-title">Contact Info</div>
  <div class="abs flag flag-us" style="left:19px;top:59px" role="img" aria-label="United States flag"></div>
  <div class="abs contact-text" style="top:62px">ORTO - VELA<br>240 Harbor Ave Suite 5<br>Miami, FL. USA</div>
  <div class="abs contact-divider"></div>
  <div class="abs flag flag-es" style="left:19px;top:148px" role="img" aria-label="Spain flag"></div>
  <div class="abs contact-text" style="top:153px">ORTO-VELA<br>Madrid, Spain</div>
</aside>

<main class="abs content-panel"></main>

<article>
  <h2 class="abs event-heading" style="left:403px;top:257px">Lorem Ipsum Dolor Sit Amet - Header for Events</h2>
  <div class="abs event-text" style="left:403px;top:311px;width:500px">
    <p><strong>Lorem ipsum dolor sit amet,</strong> consectetur adipiscing elit. Ut aliquet lacus et dolor mollis bibendum. Mauris sodales magna vel erat porttitor vel hendrerit velit lacinia. Vestibulum neque libero, placerat eget sagittis vel, vulputate eget lectus.</p>
    <p>Maecenas arcu tellus, viverra in scelerisque id, tristique eu massa. Curabitur scelerisque, urna suscipit interdum pretium, tortor nisl adipiscing lorem, quis pharetra metus orci at elit. Quisque auctor fringilla imperdiet. Maecenas sodales, erat quis sollicitudin aliquam, eros arcu fringilla mauris, sit amet tincidunt sapien quam id arcu. Nunc vitae nunc enim. Nam libero eros, pellentesque vel laoreet vitae, consequat consequat libero. Nam non lorem eu quam dictum dapibus. Praesent ut augue libero. Nulla non mauris vel nisi condimentum lobortis. In libero ante, interdum et mattis nec, venenatis a augue. Pellentesque ut ante ipsum, ullamcorper gravida turpis. Vestibulum vehicula velit in mauris consectetur in imperdiet magna semper.</p>
  </div>
  <div class="abs event-photo" role="img" aria-label="Photo of a smiling dental professional in a white coat in a bright clinic"></div>
  <div class="abs event-divider" style="top:601px"></div>
</article>

<article>
  <h2 class="abs event-heading" style="left:403px;top:640px">Lorem Ipsum Dolor Sit Amet - Header for Events</h2>
  <div class="abs event-text" style="left:403px;top:695px;width:762px">
    <p><strong>Lorem ipsum dolor sit amet,</strong> consectetur adipiscing elit. Ut aliquet lacus et dolor mollis bibendum. Mauris sodales magna vel erat porttitor vel hendrerit velit lacinia. Vestibulum neque libero, placerat eget sagittis vel, vulputate eget lectus.</p>
    <p>Maecenas arcu tellus, viverra in scelerisque id, tristique eu massa. Curabitur scelerisque, urna suscipit interdum pretium, tortor nisl adipiscing lorem, quis pharetra metus orci at elit. Quisque auctor fringilla imperdiet. Maecenas sodales, erat quis sollicitudin aliquam, eros arcu fringilla mauris, sit amet tincidunt sapien quam id arcu.</p>
  </div>
  <div class="abs event-divider" style="top:852px"></div>
</article>

<footer class="abs site-footer">
  <svg class="abs" width="1200" height="152" viewBox="0 0 1200 152" aria-hidden="true">
    <path d="M0 120 C300 60 700 150 1200 70" fill="none" stroke="rgba(0,0,0,.2)" stroke-width="40"/>
    <path d="M0 20 C400 60 800 0 1200 30" fill="none" stroke="rgba(255,255,255,.06)" stroke-width="24"/>
  </svg>
  <div class="abs footer-note">Orto-Vela ® All Rights Reserved</div>
</footer>

</body>
</html>
```